Basic Website Design for Healthcare Services Startup

We need a professional designer to take our existing basic mobile website and create professional mobile and desktop website designs. We need the designer to use the existing content and page structure at our current mobile website (http://www.valtrix.com/phone/index.html) for the new design. Let us know if you have suggestions on how we can improve the site map.

The design needs to feel contemporary and clean. We need to convey a very professional operation that embraces technology. PLEASE refer to the attached brochure to understand the style and feel we want the website to have.

We want to start small and quickly iterate to a larger, final product. Initial submissions should only include a desktop homepage and a mobile homepage. I WILL PROVIDE INITIAL FEEDBACK AND COMMIT MONEY TO THE PROJECT BEFORE ASKING DESIGNERS TO COMPLETE A FULL DESIGN FOR THE ENTIRE DESKTOP AND MOBILE SITE.

We are happy to email you any stock photos you see on our current site. Please feel free to ask questions.

Please stay close to our current color scheme, but feel free to add new colors to our palette as needed.
Our blue is: #7CD9DA
Our gray is: #585751

Thanks Designers!!

Target Market(s)

Males, Ages 18-24

Industry/Entity Type

Health Care

Number of Pages Required

5+ page

Font styles to use
Sans Serif

Requirements
Must have
• -Final design must contain all content on www.valtrix.com/phone/ website.
• -All graphics/designs/content must be easily accessible in the final deliverable so we can import it into Adobe Muse for development.
• -Must be designed in Adobe.
• -Please specify different states: normal, rollover, active, etc.
• ***UPDATE***
• Thank you everyone for your submissions! I am very happy with the quality of submissions so I will commit to the guarantee. Please focus on my comments and submit your best 2 or 3 designers. I want to give strong feedback to all designers and it is difficult when there are many different combinations of the same design elements.
• A few quick notes to help guide future submissions:
• 1.) PICTURE CONTENT: right now the focus is on designing the landing page for our donors, so the audience is 18-24 males. We want a few medical pictures, but we mostly want to connect with our donor base. Please save the pictures of doctors for the HOSPITAL PAGE. For this main page we either want to see black or hispanic people donating blood, having fun, or being with friends and loved ones.
• 2.) HOMEPAGE CONTENT: Please use the content on www.valtrix.com/phone/index.html for homepage content guidance. We do not want to include a lot of the hospital brochure content on the homepage we want that content on the HOSPITAL PAGE).
• 3.) BLOG CONTENT: Add a section for articles/blog content. We want to feature the most recent post and small previews of the previous 2 or 3 articles.
• 4.) SOCIAL: we want our social media icons to be prominent. Either in the header or at the top of the page.
• 5.) NO PARTNERS: we don't want to include our partners on the donor homepage.
• ***UPDATE***
• Hi everyone, quick clarification. The final winner will need to include all these pages. Most of them should be very quick because they do not have a lot of content on them. Please focus on the donor homepage. I will approve the look and feel before asking you to create the rest of the pages. Please note I need both Desktop and
• Mobile versions of these designs:
• Pages Needed in final design:
• -Homepage <= 85% of design work should be on this page
• -Registration
• -Hospital
• -Donor Eligibility
• -How Valtrix Works
• -Learn About PBSC Donation
• -Learn About Blood Cancer
• -About Us
Nice to have
• -Nice to have an idea how we can make your design responsive.
Should not have
• None.

```html
<!DOCTYPE html>
<html lang="en">
<head>
<meta charset="utf-8">
<title>Valtrix — Donate Blood Stem Cells</title>
<link href="https://fonts.googleapis.com/css2?family=Open+Sans:ital,wght@0,300;0,400;0,600;0,700;1,400&family=Raleway:wght@300;400;600;700&display=swap" rel="stylesheet">
<style>
:root{
  --teal:#7CD9DA;
  --teal-dark:#4fbfc1;
  --gray:#585751;
  --gray-dark:#3d3c38;
  --gray-darker:#2e2d2a;
  --text:#6b6a64;
  --light:#f2f2f1;
  --white:#ffffff;
}
*{box-sizing:border-box;margin:0;padding:0}
html,body{width:1200px;height:2728px;overflow:hidden}
body{position:relative;background:var(--white);font-family:"Open Sans",Arial,sans-serif;color:var(--text)}
.wrap{position:absolute;left:64px;width:1072px}
h2,h3,.display{font-family:"Raleway","Open Sans",sans-serif}
.btn{display:inline-block;background:var(--teal);color:var(--white);font-size:13px;font-weight:600;letter-spacing:1px;text-transform:uppercase;padding:12px 26px;border-radius:22px}
.btn-sm{font-size:10px;padding:6px 14px;border-radius:12px}

/* header */
.site-header{position:absolute;top:0;left:0;width:1200px;height:120px}
.brand{position:absolute;left:64px;top:34px;display:flex;align-items:center;gap:12px}
.brand-dot{width:46px;height:46px;border-radius:50%;border:3px solid var(--teal)}
.brand-name{font-family:"Raleway",sans-serif;font-size:30px;font-weight:600;letter-spacing:4px;color:var(--teal)}
.contact-top{position:absolute;right:64px;top:24px;text-align:right}
.phone{font-family:"Raleway",sans-serif;font-size:30px;font-weight:600;color:var(--gray);display:flex;align-items:center;justify-content:flex-end;gap:16px}
.socials{display:flex;gap:8px}
.socials span{width:28px;height:28px;border-radius:50%;background:var(--teal)}
.email{font-size:13px;color:var(--text);margin-top:6px}

/* nav */
.main-nav{position:absolute;top:120px;left:64px;width:1072px;height:52px;background:var(--teal);display:flex;align-items:stretch}
.main-nav a{color:var(--white);text-decoration:none;font-size:12px;font-weight:600;letter-spacing:.5px;text-transform:uppercase;display:flex;align-items:center;padding:0 14px}
.main-nav a.active{background:var(--teal-dark)}

/* hero */
.hero{position:absolute;top:172px;left:0;width:1200px;height:548px}
.hero-photo{position:absolute;inset:0;background:linear-gradient(100deg,#f4f6f6 0%,#e9eeee 38%,#cfe7e8 62%,#9fd7d9 82%,#d9dede 100%)}
.hero-copy{position:absolute;left:64px;top:84px;width:560px;color:var(--gray)}
.hero-copy .kicker{font-family:"Raleway",sans-serif;font-size:44px;font-weight:300;letter-spacing:1px}
.hero-copy .amount{font-family:"Raleway",sans-serif;font-size:70px;font-weight:600;line-height:1;margin-top:4px}
.hero-copy .pitch{font-family:"Raleway",sans-serif;font-size:26px;font-weight:400;text-transform:uppercase;line-height:1.2;margin-top:30px}
.hero-copy .btn{margin-top:42px}

/* welcome */
.welcome{top:750px;height:440px}
.section-title{font-size:24px;font-weight:600;color:var(--gray);letter-spacing:1px;text-transform:uppercase}
.title-rule{width:56px;height:3px;background:var(--teal);margin:12px 0 18px}
.welcome-intro{width:600px;font-size:14px;line-height:1.7}
.welcome-cols{display:flex;gap:40px;width:600px;margin-top:28px}
.welcome-cols div{flex:1}
.welcome-cols h3{font-size:15px;font-weight:700;color:var(--gray);text-transform:uppercase;margin-bottom:10px}
.welcome-cols p{font-size:13px;line-height:1.7}
.welcome-cols .btn{margin-top:14px}
.quote{position:absolute;left:680px;top:0;width:392px}
.quote-box{background:var(--teal);color:var(--white);font-style:italic;font-size:17px;line-height:1.55;padding:30px 34px;border-radius:4px;position:relative}
.quote-box::after{content:"";position:absolute;left:40px;bottom:-16px;border:16px solid transparent;border-top-color:var(--teal);border-bottom:0}
.quote-who{display:flex;align-items:center;gap:14px;margin-top:30px;padding-left:20px}
.avatar{width:64px;height:64px;border-radius:50%;background:linear-gradient(135deg,#c9a88e,#8d6c58)}
.quote-who strong{display:block;color:var(--teal-dark);font-size:16px}
.quote-who small{font-size:12px}

/* why */
.why{position:absolute;top:1200px;left:0;width:1200px;height:440px;background:var(--light)}
.center-title{display:flex;align-items:center;justify-content:center;gap:20px;padding-top:46px}
.center-title::before,.center-title::after{content:"";width:110px;height:1px;background:#c8c8c4}
.cards{position:absolute;left:64px;top:124px;width:1072px;display:flex;gap:22px;align-items:flex-start}
.card{flex:1;text-align:center;padding:26px 16px 24px;border-radius:6px}
.card.featured{background:var(--teal);color:var(--white);margin-top:-24px;padding-top:40px;padding-bottom:40px;box-shadow:0 6px 18px rgba(0,0,0,.12)}
.card-icon{width:76px;height:76px;border-radius:50%;border:2px solid var(--teal);margin:0 auto 18px;display:flex;align-items:center;justify-content:center;background:var(--white)}
.card h3{font-size:17px;font-weight:700;color:var(--gray);text-transform:uppercase;letter-spacing:1px}
.card.featured h3{color:var(--white)}
.card p{font-size:12px;line-height:1.6;margin:12px 0 16px}
.card.featured .btn{background:var(--white);color:var(--teal-dark)}

/* band */
.band{position:absolute;top:1640px;left:0;width:1200px;height:60px;background:var(--gray);color:var(--white);display:flex;align-items:center;justify-content:center;font-family:"Raleway",sans-serif;font-size:24px;font-weight:600;letter-spacing:1px;text-transform:uppercase}

/* video + stats */
.video{position:absolute;left:64px;top:1730px;width:540px;height:370px;background:linear-gradient(135deg,#6a6c6e,#3d4042 70%,#2f3133)}
.play{position:absolute;left:50%;top:42%;transform:translate(-50%,-50%)}
.video-caption{position:absolute;left:0;bottom:0;width:100%;background:var(--teal);color:var(--white);font-size:13px;font-weight:700;text-transform:uppercase;padding:12px 18px;line-height:1.4}
.stats{position:absolute;left:640px;top:1740px;width:496px;display:grid;grid-template-columns:1fr 1fr;gap:26px 28px}
.stat{display:flex;gap:12px;align-items:flex-start;font-size:13px;line-height:1.5}
.stat i{flex:none;width:36px;height:36px;border-radius:50%;border:2px solid var(--teal);position:relative}
.stat i::after{content:"";position:absolute;left:12px;top:9px;width:8px;height:13px;border:solid var(--teal);border-width:0 2px 2px 0;transform:rotate(40deg)}
.stats-btn{position:absolute;left:780px;top:2020px}

/* blog + involved */
.blog{top:2140px;width:640px}
.posts{display:flex;gap:32px}
.post{flex:1}
.post h4{font-size:16px;font-weight:700;color:var(--gray);line-height:1.3}
.post .by{font-size:11px;color:var(--teal-dark);margin:6px 0 10px}
.post p{font-size:12px;line-height:1.6}
.involved{position:absolute;left:744px;top:2140px;width:392px}
.involve-item{display:flex;align-items:center;gap:20px;margin-bottom:24px}
.ring{flex:none;width:92px;height:92px;border-radius:50%;border:3px solid var(--teal);display:flex;align-items:center;justify-content:center}
.involve-item strong{display:block;font-size:18px;font-weight:600;color:var(--gray)}
.involve-item small{font-size:12px}

/* footer */
.site-footer{position:absolute;top:2480px;left:0;width:1200px;height:208px;background:var(--gray-dark);color:#c9c8c2}
.foot-cols{position:absolute;left:64px;top:28px;width:1072px;display:grid;grid-template-columns:1fr 1fr 1fr 1.2fr;gap:24px}
.foot-cols h5{font-size:13px;font-weight:700;color:var(--white);text-transform:uppercase;letter-spacing:1px;margin-bottom:12px}
.foot-cols ul{list-style:none;columns:2;font-size:12px;line-height:2}
.foot-cols .single{columns:1}
.foot-contact{font-size:12px;line-height:1.8}
.bottom-bar{position:absolute;top:2688px;left:0;width:1200px;height:40px;background:var(--gray-darker);color:#a9a8a2;font-size:12px}
.bottom-bar .copy{position:absolute;left:64px;top:12px}
.bottom-bar .stay{position:absolute;right:64px;top:8px;display:flex;align-items:center;gap:8px}
.bottom-bar .stay span{width:22px;height:22px;border-radius:50%;background:var(--teal)}
</style>
</head>
<body>

<header class="site-header">
  <div class="brand"><span class="brand-dot"></span><span class="brand-name">VALTRIX</span></div>
  <div class="contact-top">
    <div class="phone">202.555.0148 <span class="socials"><span></span><span></span><span></span></span></div>
    <div class="email">registration@valtrix.com</div>
  </div>
</header>

<nav class="main-nav">
  <a class="active">Home</a><a>Registration</a><a>Hospital</a><a>Donor Eligibility</a><a>How Valtrix Works</a><a>Learn About PBSC Donation</a><a>Learn About Blood Cancer</a><a>About Us</a>
</nav>

<section class="hero">
  <div class="hero-photo" role="img" aria-label="Photo of a smiling young donor reclining in a clinic chair while giving blood"></div>
  <div class="hero-copy">
    <div class="kicker">DONATE BLOOD</div>
    <div class="amount">EARN $2,000</div>
    <div class="pitch">Register to donate blood stem cells and join the fight against cancer!</div>
    <span class="btn">Register Today</span>
  </div>
</section>

<section class="wrap welcome">
  <h2 class="section-title">Welcome to Valtrix</h2>
  <div class="title-rule"></div>
  <p class="welcome-intro">Valtrix is an independent bone marrow registry focused on finding donors for African American, Asian, and Hispanic patients. We are currently based out of Washington DC.</p>
  <div class="welcome-cols">
    <div>
      <h3>Our Mission</h3>
      <p>Valtrix believes that all bone marrow transplant patients should have a donor match delivered on time at an affordable price. To that end we are building a world class registry to help Transplant Centers treat their minority patients.</p>
      <span class="btn btn-sm">Read More</span>
    </div>
    <div>
      <h3>What We Do</h3>
      <p>As a total transplant procurement solution, Valtrix vertically integrates as a registry and donation center to maximize efficiency and provide operational excellence to deliver matched PBSCs on time, in minutes.</p>
      <span class="btn btn-sm">Read More</span>
    </div>
  </div>
  <div class="quote">
    <div class="quote-box">"Donating to a stranger has been an honor in a privilege. There are no words to describe the satisfaction knowing that someone is living life with the opportunity for a second chance at life."</div>
    <div class="quote-who">
      <div class="avatar" role="img" aria-label="Portrait of donor Maya"></div>
      <div><strong>MAYA</strong><small>Donated October 2013</small></div>
    </div>
  </div>
</section>

<section class="why">
  <h2 class="section-title center-title">Why Choose Valtrix</h2>
  <div class="cards">
    <div class="card">
      <div class="card-icon"><svg width="36" height="36" viewBox="0 0 36 36" fill="none" stroke="#7CD9DA" stroke-width="2"><path d="M18 4 L30 10 V20 C30 27 24 31 18 33 C12 31 6 27 6 20 V10 Z"/><path d="M12 18 l4 4 8-8"/></svg></div>
      <h3>Efficient</h3>
      <p>Increase donor availability from our dramatically secured registry.</p>
      <span class="btn btn-sm">Read More</span>
    </div>
    <div class="card">
      <div class="card-icon"><svg width="36" height="36" viewBox="0 0 36 36" fill="none" stroke="#7CD9DA" stroke-width="2"><circle cx="18" cy="18" r="14"/><circle cx="18" cy="18" r="8"/><circle cx="18" cy="18" r="2" fill="#7CD9DA"/></svg></div>
      <h3>Targeted</h3>
      <p>Donor base recruitment focusing on minority males 18-24 years old.</p>
      <span class="btn btn-sm">Read More</span>
    </div>
    <div class="card featured">
      <div class="card-icon"><svg width="36" height="36" viewBox="0 0 36 36" fill="none" stroke="#7CD9DA" stroke-width="2"><circle cx="18" cy="18" r="14"/><path d="M18 9 V18 L24 22"/></svg></div>
      <h3>Responsive</h3>
      <p>24/7 access to a personal Valtrix donation coordinator from initial match.</p>
      <span class="btn btn-sm">Read More</span>
    </div>
    <div class="card">
      <div class="card-icon"><svg width="36" height="36" viewBox="0 0 36 36" fill="none" stroke="#7CD9DA" stroke-width="2"><path d="M18 6 a9 9 0 0 1 6 16 v4 h-12 v-4 a9 9 0 0 1 6-16z"/><path d="M14 30 h8"/></svg></div>
      <h3>Intelligent</h3>
      <p>Secure, intuitive website to easily search the Valtrix database &amp; network.</p>
      <span class="btn btn-sm">Read More</span>
    </div>
    <div class="card">
      <div class="card-icon"><svg width="36" height="36" viewBox="0 0 36 36" fill="none" stroke="#7CD9DA" stroke-width="2"><rect x="6" y="12" width="24" height="17" rx="2"/><path d="M13 12 V8 h10 v4"/></svg></div>
      <h3>Professional</h3>
      <p>HCT/P transport provided by a dedicated Valtrix team member.</p>
      <span class="btn btn-sm">Read More</span>
    </div>
  </div>
</section>

<div class="band">You are desperately needed to save a life</div>

<div class="video" role="img" aria-label="Video still of donor Marcus telling his story">
  <svg class="play" width="84" height="84" viewBox="0 0 84 84"><circle cx="42" cy="42" r="40" fill="rgba(255,255,255,.9)"/><path d="M34 26 L60 42 L34 58 Z" fill="#585751"/></svg>
  <div class="video-caption">Learn more about stem cell donations. Watch Marcus's story to help a little girl</div>
</div>

<div class="stats">
  <div class="stat"><i></i><span>1 in 3 minority blood cancer patients cannot find a donor.</span></div>
  <div class="stat"><i></i><span>You might be the ONLY person that can save someone's life.</span></div>
  <div class="stat"><i></i><span>Matches usually occur between people of the same race.</span></div>
  <div class="stat"><i></i><span>Over 3,000 Americans need a blood stem cell donation each year.</span></div>
  <div class="stat"><i></i><span>Valtrix recruits donors for African American, Asian, &amp; Hispanic communities.</span></div>
</div>
<span class="btn stats-btn">Register Today</span>

<section class="wrap blog">
  <h2 class="section-title">Recent Blog Posts</h2>
  <div class="title-rule"></div>
  <div class="posts">
    <div class="post">
      <h4>Lorem ipsum dolor sit ac amet, consectet dolor adipiscing elt</h4>
      <div class="by">Posted by Jane Smith</div>
      <p>Duis autem vel eum iriure dolor in hendrerit in vulputate velit esse molestie consequat, vel illum dolore eu feugiat nulla facilisis at vero eros accumsan.</p>
    </div>
    <div class="post">
      <h4>Lorem ipsum dolor sit ac amet, consectet dolor adipiscing elt</h4>
      <div class="by">Posted by Jane Smith</div>
      <p>Duis autem vel eum iriure dolor in hendrerit in vulputate velit esse molestie consequat, vel illum dolore eu feugiat nulla facilisis at vero eros accumsan.</p>
    </div>
  </div>
</section>

<section class="involved">
  <h2 class="section-title">Get Involved</h2>
  <div class="title-rule"></div>
  <div class="involve-item">
    <div class="ring"><svg width="40" height="40" viewBox="0 0 40 40" fill="none" stroke="#7CD9DA" stroke-width="2"><circle cx="20" cy="14" r="7"/><path d="M7 35 c2-9 24-9 26 0"/></svg></div>
    <div><strong>Become a H.E.R.O</strong><small>(Higher Education Recruitment Organizer)</small></div>
  </div>
  <div class="involve-item">
    <div class="ring"><svg width="40" height="40" viewBox="0 0 40 40" fill="none" stroke="#7CD9DA" stroke-width="2"><circle cx="13" cy="15" r="5"/><circle cx="27" cy="15" r="5"/><path d="M4 33 c1-7 17-7 18 0 M18 33 c1-7 17-7 18 0"/></svg></div>
    <div><strong>Organize a Donor Drive</strong></div>
  </div>
</section>

<footer class="site-footer">
  <div class="foot-cols">
    <div><h5>Quick Links</h5><ul><li>Homepage</li><li>Registration</li><li>Hospital</li><li>Donor Eligibility</li><li>How Valtrix Works</li><li>PBSC Donation</li><li>Blood Cancer</li><li>About Us</li></ul></div>
    <div><h5>Why Choose Us</h5><ul class="single"><li>Efficient</li><li>Targeted</li><li>Intelligent</li><li>Professional</li></ul></div>
    <div><h5>Other Links</h5><ul><li>About Us</li><li>News</li><li>Terms of Use</li><li>Legal</li><li>FAQ</li><li>Blog</li><li>Careers</li><li>Privacy Policy</li></ul></div>
    <div><h5>Contact Information</h5><p class="foot-contact">1710 Park Street NW<br>Washington, DC 20010<br>202.555.0148<br>registration@valtrix.com</p></div>
  </div>
</footer>
<div class="bottom-bar">
  <span class="copy">Copyright © 2015 Valtrix LLC. All Rights Reserved</span>
  <span class="stay">Stay Connected <span></span><span></span><span></span></span>
</div>

</body>
</html>
```